Graphics for Vorlani telehealth weight loss plans

Vorlani focuses on delivering medical weight-loss using prescription medicine and telehealth consults. Vorlani needs graphics for its ecommerce site for three weight loss plans. The plans are posted here with current graphics and descriptions of what is included with each plan. Please do not feel constrained by current graphics or styling.

- https://shop.vorlanicare.com/products/steady-horizon-plan
- https://shop.vorlanicare.com/products/amber-ridge-plan
- https://shop.vorlanicare.com/products/calm-harbor-plan

The graphics need to look good on mobile and desktop browsers.

```html
<!DOCTYPE html>
<html lang="en">
<head>
<meta charset="utf-8">
<title>Vorlani weight loss plan graphics</title>
<link rel="stylesheet" href="https://fonts.googleapis.com/css2?family=Work+Sans:wght@400;500;700&display=swap">
<style>
:root{
  --bg:#000;
  --ink:#1d5c78;
  --white:#fff;
  --silver-a:#c8c8c8;
  --silver-b:#f6f6f6;
  --silver-c:#d4d4d4;
  --green:#00a38a;
  --green-edge:#c9e9e2;
  --navy:#184b6d;
  --teal-deep:#1b5565;
  --teal-mid:#1f5c6e;
}
*{box-sizing:border-box;margin:0;padding:0}
html,body{width:1200px;height:580px;overflow:hidden;background:var(--bg)}
body{position:relative;font-family:"Work Sans",Arial,sans-serif}
.plan-card{position:absolute;top:98px;width:292px;height:378px;overflow:hidden}
.card-amber{left:90px}
.card-calm{left:454px}
.card-steady{left:818px}
.card-photo{position:absolute;left:0;top:93px;width:100%;height:285px}
.card-amber .card-photo{background:radial-gradient(ellipse at 50% 55%,#2a6585 0%,var(--navy) 70%)}
.card-calm .card-photo{background:radial-gradient(ellipse at 45% 70%,#2f6e72 0%,var(--teal-deep) 70%)}
.card-steady .card-photo{background:radial-gradient(ellipse at 40% 60%,#2b6d7a 0%,var(--teal-mid) 70%)}
.card-header{position:absolute;left:0;top:0;width:100%;height:93px;
  background:linear-gradient(180deg,var(--silver-a) 0%,var(--silver-b) 28%,var(--silver-c) 55%,var(--silver-b) 80%,#e2e2e2 100%)}
.brand-name{position:absolute;left:14px;top:32px;font-weight:500;font-size:23px;color:var(--ink);letter-spacing:.5px}
.plan-title{position:absolute;left:112px;top:16px;font-weight:700;font-size:21px;line-height:21.5px;color:var(--ink)}
.includes-heading{position:absolute;left:0;width:100%;display:flex;justify-content:center;align-items:center;gap:6px;
  color:var(--white);font-size:21px;font-weight:500}
.includes-heading svg{width:24px;height:28px}
.feature-band{position:absolute;left:0;width:100%;display:flex;align-items:center;
  background:linear-gradient(180deg,#e4e4e4 0%,#fff 35%,#f2f2f2 70%,#dcdcdc 100%);
  color:var(--ink);font-weight:700;font-size:16px;letter-spacing:.3px}
.feature-band svg{position:absolute;left:11px;width:33px;height:28px}
.feature-band span{position:absolute;left:55px}
.card-steady .feature-band span{left:56px}
.nutrition-item{position:absolute;left:0;width:100%}
.nutrition-item::before{content:"";position:absolute;left:0;right:0;top:50%;height:2px;background:var(--green)}
.nutrition-box{position:absolute;left:39px;width:203px;top:0;bottom:0;background:var(--green);
  box-shadow:2px 2px 0 var(--green-edge);color:var(--white);font-size:11px;line-height:13px;
  padding:0 10px;display:flex;align-items:center;letter-spacing:.2px}
.billing{position:absolute;color:var(--white);font-weight:700;letter-spacing:.2px}
.billing svg{position:absolute}
.card-amber .billing{left:0;width:100%;top:245px;text-align:center;font-size:14.5px;line-height:17px}
.card-amber .billing svg{left:116px;top:0;width:62px;height:70px}
.card-amber .billing p{padding-top:78px}
.card-calm .billing{left:38px;top:288px;font-size:14.5px;line-height:16.5px}
.card-calm .billing svg{left:0;top:0;width:64px;height:70px}
.card-calm .billing p{position:absolute;left:72px;top:16px;white-space:nowrap}
.card-steady .billing{left:54px;top:330px;font-size:14px;line-height:16.5px}
.card-steady .billing svg{left:0;top:0;width:38px;height:42px}
.card-steady .billing p{position:absolute;left:44px;top:4px;white-space:nowrap}
</style>
</head>
<body>
<svg width="0" height="0" style="position:absolute" aria-hidden="true">
  <defs>
    <symbol id="icon-clipboard" viewBox="0 0 24 28">
      <rect x="1.5" y="3.5" width="17" height="22" rx="1.5" fill="none" stroke="#fff" stroke-width="2"/>
      <rect x="6" y="1" width="8" height="4" rx="1" fill="#fff"/>
      <path d="M4.5 10l1.5 1.5 2.5-3M4.5 15l1.5 1.5 2.5-3M4.5 20l1.5 1.5 2.5-3" fill="none" stroke="#fff" stroke-width="1.5"/>
      <path d="M10 10h6M10 15h6M10 20h4" stroke="#fff" stroke-width="1.5"/>
      <circle cx="19" cy="22" r="4.5" fill="#fff"/>
    </symbol>
    <symbol id="icon-consult" viewBox="0 0 33 28">
      <circle cx="4" cy="4" r="3" fill="currentColor"/>
      <circle cx="29" cy="4" r="3" fill="currentColor"/>
      <path d="M1 9h5v8h5v10H8v-7H2z" fill="currentColor"/>
      <path d="M32 9h-5v8h-5v10h3v-7h6z" fill="currentColor"/>
      <rect x="10" y="12" width="13" height="3" fill="currentColor"/>
      <rect x="15" y="15" width="3" height="12" fill="currentColor"/>
    </symbol>
    <symbol id="icon-capsule" viewBox="0 0 33 28">
      <g transform="rotate(-40 14 15)">
        <rect x="1" y="10" width="26" height="11" rx="5.5" fill="currentColor"/>
        <rect x="14" y="11.5" width="11.5" height="8" rx="4" fill="#fff"/>
      </g>
      <circle cx="25" cy="17" r="7" fill="currentColor"/>
      <path d="M19 19l12-4" stroke="#fff" stroke-width="1.6"/>
    </symbol>
    <symbol id="icon-renew" viewBox="0 0 62 70">
      <path d="M14 58A26 26 0 0 1 31 9" fill="none" stroke="#fff" stroke-width="3.5"/>
      <path d="M26 2l11 7-11 8z" fill="#fff"/>
      <path d="M48 12A26 26 0 0 1 31 61" fill="none" stroke="#fff" stroke-width="3.5"/>
      <path d="M36 68l-11-7 11-8z" fill="#fff"/>
      <rect x="17" y="21" width="28" height="26" rx="3" fill="none" stroke="#fff" stroke-width="3"/>
      <rect x="17" y="21" width="28" height="6" fill="#fff"/>
      <path d="M23 18v6M39 18v6" stroke="#fff" stroke-width="3"/>
      <g fill="#fff">
        <rect x="21" y="30" width="4" height="3"/><rect x="27" y="30" width="4" height="3"/><rect x="33" y="30" width="4" height="3"/><rect x="39" y="30" width="3" height="3"/>
        <rect x="21" y="35" width="4" height="3"/><rect x="27" y="35" width="4" height="3"/><rect x="33" y="35" width="4" height="3"/><rect x="39" y="35" width="3" height="3"/>
        <rect x="21" y="40" width="4" height="3"/><rect x="27" y="40" width="4" height="3"/><rect x="33" y="40" width="4" height="3"/>
      </g>
    </symbol>
  </defs>
</svg>

<section class="plan-card card-amber">
  <div class="card-photo" role="img" aria-label="Photo of scattered capsules in blue tones"></div>
  <header class="card-header">
    <div class="brand-name">Vorlani</div>
    <h2 class="plan-title">Amber Ridge<br>Plan</h2>
  </header>
  <h3 class="includes-heading" style="top:102px"><svg><use href="#icon-clipboard"/></svg>Plan Includes:</h3>
  <div class="feature-band" style="top:139px;height:37px"><svg><use href="#icon-consult"/></svg><span>PHYSICIAN CONSULTANT</span></div>
  <div class="feature-band" style="top:186px;height:36px"><svg><use href="#icon-capsule"/></svg><span>PHENTERMINE PROGRAM</span></div>
  <div class="billing"><svg><use href="#icon-renew"/></svg><p>MONTH TO MONTH<br>PAY AS YOU GO</p></div>
</section>

<section class="plan-card card-calm">
  <div class="card-photo" role="img" aria-label="Photo of a bowl of fresh vegetables in teal tones"></div>
  <header class="card-header">
    <div class="brand-name">Vorlani</div>
    <h2 class="plan-title">Calm Harbor<br>Plan</h2>
  </header>
  <h3 class="includes-heading" style="top:102px"><svg><use href="#icon-clipboard"/></svg>Plan Includes:</h3>
  <div class="nutrition-item" style="top:142px;height:20px"><div class="nutrition-box">Expert Nutrition consult</div></div>
  <div class="nutrition-item" style="top:177px;height:31px"><div class="nutrition-box">Custom crafted diet plan<br>to achieve your goals</div></div>
  <div class="nutrition-item" style="top:222px;height:30px"><div class="nutrition-box">Nutritionist coaching to improve<br>your health and vitality</div></div>
  <div class="billing"><svg><use href="#icon-renew"/></svg><p>MONTH TO MONTH<br>PAY AS YOU GO</p></div>
</section>

<section class="plan-card card-steady">
  <div class="card-photo" role="img" aria-label="Photo of a person measuring their waist in teal tones"></div>
  <header class="card-header">
    <div class="brand-name">Vorlani</div>
    <h2 class="plan-title">Steady Horizon<br>Plan</h2>
  </header>
  <h3 class="includes-heading" style="top:100px"><svg><use href="#icon-clipboard"/></svg>Plan Includes:</h3>
  <div class="feature-band" style="top:135px;height:33px"><svg><use href="#icon-consult"/></svg><span>PHYSICIAN CONSULTANT</span></div>
  <div class="feature-band" style="top:177px;height:33px"><svg><use href="#icon-capsule"/></svg><span>PHENTERMINE PROGRAM</span></div>
  <div class="nutrition-item" style="top:221px;height:20px"><div class="nutrition-box">Expert Nutrition consult</div></div>
  <div class="nutrition-item" style="top:250px;height:33px"><div class="nutrition-box">Custom crafted diet plan<br>to achieve your goals</div></div>
  <div class="nutrition-item" style="top:290px;height:32px"><div class="nutrition-box">Nutritionist coaching to improve<br>your health and vitality</div></div>
  <div class="billing"><svg><use href="#icon-renew"/></svg><p>MONTH TO MONTH<br>PAY AS YOU GO</p></div>
</section>
</body>
</html>
```